Business Cards

The name of our firm is "Tallpine Insurance adjusters"
We separate ourselves from all other public adjusters because most of us worked for the insurance companies so we understand their games.
As Insurance adjusters we represent the Insured, not the insurance companies. Our # 1 priority is to handle the entire claim process as seamless as possible on behalf of the homeowner/business owner so they don't have to deal with the hassles and headaches. Just as the logo your team designed, I want the cards to stand out from everyone elses. I also want the cards to help better understand our services and Value on hiring us and value that we can offer.
I uploaded the logo whenever I created the project. I don't see an option on re uploading the logo anywhere. Any advise??

```html
<!DOCTYPE html>
<html lang="en">
<head>
<meta charset="utf-8">
<title>Tallpine Insurance Adjusters – Business Cards</title>
<link href="https://fonts.googleapis.com/css2?family=Montserrat:wght@700&family=Arimo:wght@400&display=swap" rel="stylesheet">
<style>
  :root {
    --backdrop: #2b2b2b;
    --card-dark: #131313;
    --card-light: #ffffff;
    --brand-blue: #1a6ea6;
    --brand-blue-deep: #0f5a8c;
    --ink: #1d1d1d;
  }
  * { box-sizing: border-box; margin: 0; padding: 0; }
  html, body {
    width: 1200px; height: 1015px; overflow: hidden;
    background: var(--backdrop);
  }
  .sheet {
    width: 1200px; height: 1015px;
    display: flex; flex-direction: column; align-items: center; justify-content: center;
    gap: 40px;
  }
  .card {
    width: 760px; height: 434px; position: relative;
    box-shadow: 0 10px 28px rgba(0,0,0,.45);
  }
  /* Front */
  .card-front {
    background: var(--card-dark);
    display: flex; align-items: center; justify-content: center;
  }
  .brand {
    display: flex; align-items: center; gap: 14px;
    font-family: "Montserrat", sans-serif; font-weight: 700;
    color: var(--brand-blue);
    text-transform: uppercase;
  }
  .brand-dot {
    width: 22px; height: 22px; border-radius: 50%;
    background: var(--brand-blue); flex: none;
  }
  .brand-front .brand-name { font-size: 40px; line-height: 1.1; letter-spacing: 1px; }
  .brand-front .brand-name span { display: block; font-size: 17px; letter-spacing: 3px; }

  /* Back */
  .card-back { background: var(--card-light); }
  .brand-back {
    position: absolute; right: 60px; top: 70px;
  }
  .brand-back .brand-name { font-size: 32px; line-height: 1.1; letter-spacing: 1px; }
  .brand-back .brand-name span { display: block; font-size: 13px; letter-spacing: 2.5px; }
  .brand-back .brand-dot { width: 18px; height: 18px; }

  .divider {
    position: absolute; left: 40px; right: 40px; top: 212px;
    height: 2px; background: var(--brand-blue);
  }
  .holder-name {
    position: absolute; left: 40px; top: 166px;
    font-family: "Montserrat", sans-serif; font-weight: 700;
    font-size: 34px; letter-spacing: 1px; color: var(--brand-blue-deep);
    text-transform: uppercase;
  }
  .contacts {
    position: absolute; left: 40px; top: 240px;
    list-style: none;
    font-family: "Arimo", sans-serif; font-size: 22px; color: var(--ink);
    display: flex; flex-direction: column; gap: 12px;
  }
  .contacts li { display: flex; align-items: center; gap: 14px; }
  .contacts svg { width: 24px; height: 24px; flex: none; }
  .address {
    position: absolute; right: 40px; top: 240px; text-align: right;
    font-family: "Arimo", sans-serif; font-size: 22px; line-height: 1.45; color: var(--ink);
  }
</style>
</head>
<body>
<main class="sheet">
  <section class="card card-front">
    <div class="brand brand-front">
      <div class="brand-dot"></div>
      <div class="brand-name">Tallpine<span>Insurance Adjusters</span></div>
    </div>
  </section>

  <section class="card card-back">
    <div class="brand brand-back">
      <div class="brand-dot"></div>
      <div class="brand-name">Tallpine<span>Insurance Adjusters</span></div>
    </div>

    <h1 class="holder-name">Marcus Reed</h1>
    <div class="divider"></div>

    <ul class="contacts">
      <li>
        <svg viewBox="0 0 24 24" aria-hidden="true"><path fill="var(--brand-blue)" d="M6.6 10.8a15.1 15.1 0 0 0 6.6 6.6l2.2-2.2c.3-.3.7-.4 1-.2 1.1.4 2.3.6 3.6.6.6 0 1 .4 1 1V20c0 .6-.4 1-1 1A17 17 0 0 1 3 4c0-.6.4-1 1-1h3.5c.6 0 1 .4 1 1 0 1.3.2 2.5.6 3.6.1.3 0 .7-.2 1z"/></svg>
        044-123 456 789
      </li>
      <li>
        <svg viewBox="0 0 24 24" aria-hidden="true"><rect x="2" y="5" width="20" height="14" fill="var(--brand-blue)"/><path d="M2 5l10 8 10-8" fill="none" stroke="#fff" stroke-width="1.6"/></svg>
        info@webname.com
      </li>
      <li>
        <svg viewBox="0 0 24 24" aria-hidden="true"><g fill="none" stroke="var(--brand-blue)" stroke-width="1.8"><circle cx="12" cy="12" r="9.5"/><ellipse cx="12" cy="12" rx="4" ry="9.5"/><path d="M2.5 12h19M4 7h16M4 17h16"/></g></svg>
        www.websitename.com
      </li>
    </ul>

    <address class="address" style="font-style:normal">
      421 , Address line goes here<br>
      45452,Country Name
    </address>
  </section>
</main>
</body>
</html>
```